HVAC Company Business Card design with attached logo

Looking for an easily readable and attractive business card design that includes my attached company logo. I selected one sided card because it's more traditional, but I'm open to a 2-sided design. All of the details should be included in the design. Looking to create a professional, upscale image.

Target Market(s)

Commercial and residential consumers

Industry/Entity Type

Hvac

Contact Information for Business Card

Company phone number is 631.587.0293
Company email dennis@pinecresthvac.example
Company name is Silver Pine Air Conditioning, Refrigeration, and Heating
Dennis Harlow
Owner Operator
Company Address is
PO Box 872,
527 Maplewood Rd,
Wrenfield, NH 11862
Business License K7158920000
Insured

Font styles to use
Serif
Sans Serif

Colors

Designer to choose colors to be used in the design.

Requirements
Must have
• Must include the logo.
Nice to have
• It seems like it should be a one sided card, but I'm open to a 2 sided one.

```html
<!DOCTYPE html>
<html lang="en">
<head>
<meta charset="utf-8">
<title>Silver Pine Air Conditioning and Heating – Business Card</title>
<link href="https://fonts.googleapis.com/css2?family=Montserrat:wght@300;400;600;800&display=swap" rel="stylesheet">
<style>
  :root {
    --brand-blue: #3b5fbd;
    --brand-blue-deep: #2a47a3;
    --brand-orange: #ee7a2e;
    --brand-orange-dark: #c75d18;
    --card-white: #f6f6f6;
    --backdrop: #e4e4e2;
  }
  * { margin: 0; padding: 0; box-sizing: border-box; }
  html, body {
    width: 1200px; height: 800px; overflow: hidden;
    background: var(--backdrop);
    font-family: "Montserrat", Arial, sans-serif;
  }
  .stage {
    width: 1200px; height: 800px;
    display: flex; align-items: center; justify-content: center; gap: 40px;
  }
  .card {
    position: relative;
    width: 540px; height: 309px;
    background: var(--card-white);
    overflow: hidden;
    box-shadow: 0 6px 18px rgba(0,0,0,0.12);
  }

  /* Back side */
  .card-back .edge-blue {
    position: absolute; top: 0; left: 0; right: 0; height: 9px;
    background: var(--brand-blue);
  }
  .card-back .edge-orange {
    position: absolute; bottom: 10px; left: 0; right: 0; height: 10px;
    background: var(--brand-orange);
  }
  .card-back .brand {
    position: absolute; inset: 0;
    display: flex; align-items: center; justify-content: center;
  }

  /* Logo lockup: one colour, one weight */
  .brand-lockup { display: flex; align-items: center; gap: 14px; }
  .brand-dot {
    width: 58px; height: 58px; border-radius: 50%;
    background: var(--brand-orange);
    flex: none;
  }
  .brand-name {
    color: var(--brand-blue);
    font-weight: 800;
    line-height: 1;
    text-transform: uppercase;
  }
  .brand-name .name-line { display: block; font-size: 40px; letter-spacing: 1px; }
  .brand-name .trade-line { display: block; font-size: 11px; letter-spacing: 1.6px; margin-top: 6px; }

  /* Front side */
  .card-front .field { position: absolute; inset: 0; }
  .card-front .brand-lockup { position: absolute; top: 38px; left: 36px; }
  .card-front .brand-dot { width: 46px; height: 46px; }
  .card-front .brand-name .name-line { font-size: 33px; }
  .card-front .brand-name .trade-line { font-size: 9.5px; letter-spacing: 1.2px; }

  .name-ribbon {
    position: absolute; left: 192px; top: 116px;
    width: 206px; height: 46px;
    background: var(--brand-orange);
    color: #fff; text-align: center;
    padding-top: 6px;
  }
  .name-ribbon .person { display: block; font-weight: 600; font-size: 18px; line-height: 1.1; }
  .name-ribbon .role { display: block; font-weight: 400; font-size: 9px; letter-spacing: 1.5px; }

  .contact { position: absolute; color: #fff; font-weight: 400; font-size: 12.5px; letter-spacing: 0.4px; text-transform: uppercase; white-space: nowrap; }
  .contact-row { display: flex; align-items: center; gap: 9px; margin-bottom: 6px; }
  .icon-dot {
    width: 15px; height: 15px; border-radius: 50%;
    background: var(--brand-orange);
    display: flex; align-items: center; justify-content: center; flex: none;
  }
  .contact-direct { left: 28px; bottom: 22px; }
  .contact-address { right: 20px; top: 178px; font-size: 11.5px; line-height: 1.45; }
  .contact-address .contact-row { align-items: flex-start; margin-bottom: 4px; }
  .contact-address .icon-dot { margin-top: 2px; }
  .license { padding-left: 24px; font-size: 9px; font-weight: 300; letter-spacing: 0.3px; text-transform: none; }
</style>
</head>
<body>
<main class="stage">

  <section class="card card-back" aria-label="Card back">
    <div class="edge-blue"></div>
    <div class="brand">
      <div class="brand-lockup">
        <span class="brand-dot"></span>
        <span class="brand-name">
          <span class="name-line">Silver Pine</span>
          <span class="trade-line">Air Conditioning and Heating</span>
        </span>
      </div>
    </div>
    <div class="edge-orange"></div>
  </section>

  <section class="card card-front" aria-label="Card front">
    <svg class="field" width="540" height="309" viewBox="0 0 540 309" aria-hidden="true">
      <defs>
        <linearGradient id="panelBlue" x1="0" y1="0" x2="1" y2="1">
          <stop offset="0" stop-color="#4468c4"/>
          <stop offset="1" stop-color="#2a47a3"/>
        </linearGradient>
      </defs>
      <line x1="0" y1="206" x2="540" y2="86" stroke="#3b5fbd" stroke-width="3"/>
      <polygon points="0,218 540,98 540,309 0,309" fill="url(#panelBlue)"/>
      <polygon points="180,128 192,122 192,166" fill="#c75d18"/>
      <polygon points="410,128 398,122 398,166" fill="#c75d18"/>
    </svg>

    <div class="brand-lockup">
      <span class="brand-dot"></span>
      <span class="brand-name">
        <span class="name-line">Silver Pine</span>
        <span class="trade-line">Air Conditioning and Heating</span>
      </span>
    </div>

    <div class="name-ribbon">
      <span class="person">Dennis Harlow</span>
      <span class="role">OPERATOR</span>
    </div>

    <div class="contact contact-address">
      <div class="contact-row">
        <span class="icon-dot">
          <svg width="8" height="10" viewBox="0 0 8 10" aria-hidden="true"><path d="M4 0C1.8 0 0 1.7 0 3.8 0 6.5 4 10 4 10s4-3.5 4-6.2C8 1.7 6.2 0 4 0zm0 5.2a1.4 1.4 0 1 1 0-2.8 1.4 1.4 0 0 1 0 2.8z" fill="#fff"/></svg>
        </span>
        <span>PO Box 872, 527 Maplewood<br>Rd, Wrenfield, NH 11862</span>
      </div>
      <div class="license">K7158920000 Insured</div>
    </div>

    <div class="contact contact-direct">
      <div class="contact-row">
        <span class="icon-dot">
          <svg width="9" height="9" viewBox="0 0 10 10" aria-hidden="true"><path d="M2 0.5l1.6 2.2-1 1c.6 1.3 1.5 2.2 2.8 2.8l1-1L8.6 7 8 9.2C4 9 1 6 .8 2z" fill="#fff"/></svg>
        </span>
        <span>631.587.0293</span>
      </div>
      <div class="contact-row">
        <span class="icon-dot">
          <svg width="9" height="7" viewBox="0 0 10 7" aria-hidden="true"><rect x="0.5" y="0.5" width="9" height="6" fill="none" stroke="#fff"/><path d="M0.5 0.5L5 4l4.5-3.5" fill="none" stroke="#fff"/></svg>
        </span>
        <span>dennis@pinecresthvac.example</span>
      </div>
    </div>
  </section>

</main>
</body>
</html>
```